Engaging online lending company website

We already have a website at www.brightwaycredit.com.au however it's nowhere near engaging enough. We are a fintech online brokerage company providing fantastic and super quick turnaround times on vehicle and mortgage loans. We need a website that is engaging with lots of call to actions and quote forms to capture details.

Target Market(s)

Young, technology savvy Australian's requiring finance. Aged between 20 - 45

Industry/Entity Type

Finance

Coding

Coded - Design and coding required

Requirements
Must have
• Get a Quick Quote Call to Action Box
• Get a Quick Quote (Express)
• Calculator Designs (2) – Home loan repayment and car loan repayment
• How it Works – Engaging design showing our 4 step loans process
• Banners: 1x for lending panel, 1 for current interest rates (similar to harbourline capital home page), 1x Review Nest for customer reviews
• Banner on each page: Similar to Kestrel Money “Today’s Best Rate” see below:
• Lots of well placed call to action buttons and quick quote forms on each page
• Apply Now page (similar fields to: https://www.harbourlinecapitalgroup.com.au/pre-approval/)

```html
<!DOCTYPE html>
<html lang="en">
<head>
<meta charset="utf-8">
<title>Brightway Credit – Car, Home and Commercial Loans</title>
<link rel="stylesheet" href="https://fonts.googleapis.com/css2?family=Roboto+Condensed:wght@400;700&family=Roboto:wght@300;400;500;700&display=swap">
<style>
:root{
  --navy:#173a52;
  --deep:#24566e;
  --teal:#2b6d88;
  --blue:#1ea3cf;
  --blue-dark:#1583ad;
  --pale:#eef7fb;
  --ink:#1f3444;
  --body:#4a5560;
  --white:#ffffff;
  --rule:#8aa0ad;
}
*{box-sizing:border-box;margin:0;padding:0}
html,body{width:1200px;height:2965px;overflow:hidden}
body{position:relative;background:var(--pale);font-family:"Roboto",Arial,sans-serif;color:var(--body)}
.abs{position:absolute}

/* top bar */
.topbar{left:0;top:0;width:1200px;height:20px;background:var(--navy);color:#cfe2ec;font-size:10px;display:flex;align-items:center;justify-content:center;gap:56px}
.topbar b{font-weight:700;color:#fff}

/* header */
.header{left:0;top:20px;width:1200px;height:60px;background:var(--white)}
.brand{left:250px;top:16px;width:200px;font-family:"Roboto Condensed",sans-serif;font-weight:700;font-size:24px;color:var(--blue-dark);line-height:28px;text-transform:uppercase;white-space:nowrap}
.nav{left:480px;top:23px;display:flex;gap:19px;font-family:"Roboto Condensed",sans-serif;font-size:10.5px;font-weight:700;text-transform:uppercase;color:var(--blue);white-space:nowrap}
.nav .current{color:var(--ink)}

/* hero */
.hero{left:0;top:80px;width:1200px;height:434px;background:linear-gradient(90deg,#3a3f46 0%,#9c3a3d 30%,#c9bfbb 55%,#e6d6c8 75%,#d9714a 100%)}
.cta-band{left:0;top:514px;width:1200px;height:69px;background:var(--teal);display:flex;justify-content:center;gap:38px;padding-top:12px}
.btn{display:inline-block;background:var(--blue);color:var(--white);font-family:"Roboto Condensed",sans-serif;font-weight:700;font-size:15px;text-transform:uppercase;letter-spacing:.5px;text-align:center;white-space:nowrap}
.cta-band .btn{width:190px;height:40px;line-height:40px}

/* rates */
.rates{left:0;top:583px;width:1200px;height:174px;background:var(--blue)}
.rate-card{top:24px;width:236px;height:136px;background:var(--white)}
.rate-card.today{left:245px}
.rate-card.fixed{left:496px}
.rate-card.compare{left:749px}
.today .pill{position:absolute;left:26px;top:40px;width:184px;height:40px;line-height:40px;background:var(--blue)}
.today .date{position:absolute;left:50px;top:94px;font-family:"Roboto Condensed",sans-serif;font-weight:700;color:var(--blue-dark);font-size:14px}
.rate-card .lbl{position:absolute;left:20px;top:34px;font-family:"Roboto Condensed",sans-serif;font-weight:700;font-size:13px;color:var(--ink);text-transform:uppercase}
.rate-card .val{position:absolute;left:82px;top:44px;font-family:"Roboto Condensed",sans-serif;font-weight:700;font-size:56px;color:var(--blue);line-height:60px}
.compare .val{left:70px}
.rate-card .val small{font-size:30px}
.rate-card .tag{position:absolute;right:14px;bottom:14px;font-family:"Roboto Condensed",sans-serif;font-weight:700;font-size:13px;color:var(--ink);text-transform:uppercase}

/* how it works */
.mini-brand{left:0;top:808px;width:1200px;text-align:center;font-family:"Roboto Condensed",sans-serif;font-weight:700;font-size:22px;color:var(--blue-dark);text-transform:uppercase}
.how-title{left:0;top:858px;width:1200px;text-align:center;font-family:"Roboto Condensed",sans-serif;font-size:30px;line-height:36px;text-transform:uppercase;color:var(--blue);font-weight:400}
.how-title span{display:block;color:var(--ink);font-weight:700}
.how-copy{left:290px;top:942px;width:620px;text-align:center;font-size:12.5px;line-height:17px;color:var(--blue)}
.steps{left:300px;top:1046px;width:600px;display:flex;justify-content:space-between}
.step{width:120px;text-align:center;font-family:"Roboto Condensed",sans-serif;font-size:15px;line-height:18px;color:var(--blue)}
.step .art{width:100px;height:66px;margin:0 auto 8px;background:linear-gradient(#cfe7f2,#7fc2dd);border-radius:6px}

/* loan features */
.feature h2{font-family:"Roboto Condensed",sans-serif;font-size:23px;line-height:28px;color:var(--blue);text-transform:uppercase;font-weight:400}
.feature h3{font-family:"Roboto Condensed",sans-serif;font-size:23px;line-height:28px;color:var(--ink);text-transform:uppercase;font-weight:700;margin-bottom:10px}
.feature p{font-size:11px;line-height:16px;text-align:justify;color:var(--body);margin-bottom:16px}
.feature .btn{width:196px;height:34px;line-height:34px;font-size:13px}
.photo{border:6px solid var(--white);box-shadow:0 0 0 1px #d5e3ea}
.home-text{left:249px;top:1234px;width:330px}
.home-photo{left:600px;top:1238px;width:346px;height:240px;background:linear-gradient(135deg,#202426,#6b6664 50%,#2b2e31)}
.car-text{left:621px;top:1580px;width:330px}
.car-photo{left:249px;top:1585px;width:346px;height:240px;background:linear-gradient(135deg,#c9b64a,#e6d35b 40%,#8f8a82 70%,#c0bdb8)}
.com-text{left:249px;top:1926px;width:330px}
.com-photo{left:600px;top:1928px;width:346px;height:240px;background:linear-gradient(135deg,#e9ecef,#2f3948 55%,#c9ced4)}
.divider{left:308px;width:584px;height:14px}

/* calculator band */
.calc-band{left:0;top:2306px;width:1200px;height:171px;background:var(--deep)}
.calc-art{background:linear-gradient(#d9eef7,#2fa8d3);border-radius:6px}
.calc-truck{left:251px;top:2240px;width:226px;height:135px}
.calc-device{left:583px;top:2234px;width:102px;height:140px;background:linear-gradient(#2fa8d3,#1583ad)}
.calc-house{left:785px;top:2240px;width:164px;height:135px}
.calc-title{left:0;top:2390px;width:1200px;text-align:center;font-size:26px;font-weight:300;color:var(--blue)}
.calc-copy{left:320px;top:2426px;width:560px;text-align:center;font-size:12.5px;line-height:17px;color:#d9e8ef}
.calc-copy b{color:var(--blue);font-weight:500}

/* testimonials */
.testi{left:0;top:2477px;width:1200px;height:235px;background:var(--blue);text-align:center;color:var(--white)}
.testi h2{margin-top:24px;font-family:"Roboto Condensed",sans-serif;font-weight:700;font-size:28px;letter-spacing:3px}
.avatar{width:90px;height:90px;margin:12px auto 0;border-radius:50%;border:4px solid var(--white);background:linear-gradient(#c99a7a,#e9e3de)}
.testi p{width:650px;margin:12px auto 0;font-size:12px;line-height:17px;color:#e7f5fb;letter-spacing:.5px}
.testi .name{margin-top:6px;font-family:"Roboto Condensed",sans-serif;font-weight:700;font-size:11px;text-transform:uppercase;letter-spacing:1px}

/* footer */
.footer{left:0;top:2712px;width:1200px;height:230px;background:var(--deep)}
.footer h4{font-family:"Roboto Condensed",sans-serif;font-weight:700;font-size:12px;letter-spacing:1.5px;color:var(--blue);text-transform:uppercase;margin-bottom:10px}
.links{display:grid;grid-template-columns:150px 150px;column-gap:14px}
.links a{display:block;font-size:9.5px;color:#9fc5d6;text-decoration:none;border-bottom:1px solid #3d7089;padding:4px 0 4px 12px;position:relative}
.links a::before{content:"";position:absolute;left:2px;top:9px;width:4px;height:4px;border-top:1px solid var(--blue);border-right:1px solid var(--blue);transform:rotate(45deg)}
.sell{left:250px;top:18px}
.tweets{left:578px;top:18px;width:170px}
.tweet{display:flex;gap:8px;margin-bottom:10px;font-size:9px;line-height:13px;color:#9fc5d6}
.tweet svg{flex:none;margin-top:2px}
.tweet em{display:block;font-style:normal;color:#e0eef4}
.loc{left:770px;top:18px;width:200px;font-size:9.5px;line-height:15px;color:#9fc5d6}
.loc b{color:var(--blue);font-weight:400}
.social{display:flex;gap:8px;margin-top:6px}
.social span{width:34px;height:34px;background:var(--blue);border-radius:4px}
.bottombar{left:0;top:2942px;width:1200px;height:23px;background:var(--navy);font-size:9.5px;color:#cfe2ec;padding:6px 250px}
</style>
</head>
<body>

<div class="abs topbar">
  <span><b>Phone Number :</b> 1300 482 190</span>
  <span><b>Email :</b> info@brightwaycredit.com.au</span>
  <span><b>Address :</b> Sydney New South Wales, Australia</span>
</div>

<header class="abs header">
  <div class="abs brand">Brightway Credit</div>
  <nav class="abs nav">
    <span class="current">Home</span>
    <span>Car Loans</span>
    <span>Personal Loans</span>
    <span>Commercial Loans</span>
    <span>Get a Quick Quote</span>
    <span>Contact Us</span>
  </nav>
</header>

<div class="abs hero" role="img" aria-label="Photo of one hand passing car keys and another hand holding a small model house"></div>

<div class="abs cta-band">
  <span class="btn">Get a Quick Quote</span>
  <span class="btn">Quick Quote Call</span>
  <span class="btn">Loan Repayment</span>
</div>

<section class="abs rates">
  <div class="abs rate-card today">
    <span class="btn pill">Today's Best Rate On</span>
    <span class="date">TUE MAR 07 2017</span>
  </div>
  <div class="abs rate-card fixed">
    <span class="lbl">Car loans from</span>
    <span class="val">4.4<small>%</small></span>
    <span class="tag">Fixed</span>
  </div>
  <div class="abs rate-card compare">
    <span class="lbl">Car loans from</span>
    <span class="val">5.25<small>%*</small></span>
    <span class="tag">Comparison</span>
  </div>
</section>

<div class="abs mini-brand">Brightway Credit</div>
<h1 class="abs how-title">How it Works<span>Brightway Credit</span></h1>
<p class="abs how-copy">Lorem ipsum dolor sit amet consectetur adipisicing elit, sed do eiusmod tempor incididunt ut labore et dolore magna aliqua. Ut enim ad minim veniam, quis of the printing and typesetting industry. Lorem Ipsum has been the industry standard dummy text ever since the 1500s, when an unknown printer took a galley and scrambled it to make a type specimen book. It has survived not only five centuries, remaining essentially unchanged.</p>

<div class="abs steps">
  <div class="step"><div class="art" role="img" aria-label="Illustration of a person beside a car"></div>Car<br>Loans</div>
  <div class="step"><div class="art" role="img" aria-label="Illustration of a worker beside a company car"></div>Work<br>Car Loans</div>
  <div class="step"><div class="art" role="img" aria-label="Illustration of a tradesperson beside a ute"></div>Tradie<br>Loans</div>
  <div class="step"><div class="art" role="img" aria-label="Illustration of a person beside a house"></div>Home<br>Loans</div>
</div>

<article class="abs feature home-text">
  <h2>Home Loans</h2>
  <h3>Brightway Credit</h3>
  <p>Lorem ipsum dolor sit amet consectetur adipisicing elit, sed do eiusmod tempor incididunt ut labore et dolore magna aliqua. Ut enim ad minim veniam, quis of the printing and typesetting industry. Lorem Ipsum has been the industry standard dummy text ever since the 1500s, when an unknown printer took a galley and scrambled it to make a type specimen book. It has survived not only five centuries, remaining essentially unchanged.</p>
  <span class="btn">Get a Quick Quote Call</span>
</article>
<div class="abs photo home-photo" role="img" aria-label="Photo of a hand holding a model house on a glass tile"></div>

<svg class="abs divider" style="top:1527px" viewBox="0 0 584 14" aria-hidden="true"><line x1="0" y1="7" x2="584" y2="7" stroke="#8aa0ad"/><rect x="286" y="1" width="12" height="12" transform="rotate(45 292 7)" fill="#173a52"/></svg>

<div class="abs photo car-photo" role="img" aria-label="Photo of a hand holding car keys in front of yellow cars"></div>
<article class="abs feature car-text">
  <h2>Car Loans</h2>
  <h3>Brightway Credit</h3>
  <p>Lorem ipsum dolor sit amet consectetur adipisicing elit, sed do eiusmod tempor incididunt ut labore et dolore magna aliqua. Ut enim ad minim veniam, quis of the printing and typesetting industry. Lorem Ipsum has been the industry standard dummy text ever since the 1500s, when an unknown printer took a galley and scrambled it to make a type specimen book. It has survived not only five centuries, remaining essentially unchanged.</p>
  <span class="btn">Get a Quick Quote Call</span>
</article>

<svg class="abs divider" style="top:1875px" viewBox="0 0 584 14" aria-hidden="true"><line x1="0" y1="7" x2="584" y2="7" stroke="#8aa0ad"/><rect x="286" y="1" width="12" height="12" transform="rotate(45 292 7)" fill="#173a52"/></svg>

<article class="abs feature com-text">
  <h2>Commercial Loans</h2>
  <h3>Brightway Credit</h3>
  <p>Lorem ipsum dolor sit amet consectetur adipisicing elit, sed do eiusmod tempor incididunt ut labore et dolore magna aliqua. Ut enim ad minim veniam, quis of the printing and typesetting industry. Lorem Ipsum has been the industry standard dummy text ever since the 1500s, when an unknown printer took a galley and scrambled it to make a type specimen book. It has survived not only five centuries, remaining essentially unchanged.</p>
  <span class="btn">Get a Quick Quote Call</span>
</article>
<div class="abs photo com-photo" role="img" aria-label="Photo of a businessman holding keys over a clipboard"></div>

<section class="abs calc-band"></section>
<div class="abs calc-art calc-truck" role="img" aria-label="Illustration of a mechanic beside a ute"></div>
<div class="abs calc-art calc-device" role="img" aria-label="Illustration of a calculator"></div>
<div class="abs calc-art calc-house" role="img" aria-label="Illustration of a person beside a house"></div>
<h2 class="abs calc-title">Car Loan Calculator</h2>
<p class="abs calc-copy">Want to know what your repayments might be before applying for finance? Use our car finance calculator. Don't forget, we have access to car finance rates from as low as <b>4.2%</b>!</p>

<section class="abs testi">
  <h2>TESTIMONIALS</h2>
  <div class="avatar" role="img" aria-label="Customer portrait photo"></div>
  <p>Lorem Ipsum is simply dummy text of the printing and typesetting industry. Lorem Ipsum has been the industry standard ever since, with versions of Lorem Ipsum</p>
  <div class="name">Clara Penfold</div>
</section>

<footer class="abs footer">
  <div class="abs sell">
    <h4>Selling</h4>
    <div class="links">
      <a>Customer Reviews</a><a>Insurance Quote</a>
      <a>Finance Planner</a><a>Novated Leasing</a>
      <a>FAQ</a><a>Loan Calculator</a>
      <a>About</a><a>Car Loans</a>
      <a>Contact Us</a><a>Commercial Loans</a>
      <a>Car Loans</a><a>Home Loans</a>
      <a>Personal Loans</a><a>Resources</a>
    </div>
  </div>
  <div class="abs tweets">
    <h4>Tweets</h4>
    <div class="tweet"><svg width="10" height="10" viewBox="0 0 10 10" aria-hidden="true"><path d="M1 5l3 3 5-7" stroke="#1ea3cf" stroke-width="1.5" fill="none"/></svg><div>New low car loan rates now live for approved buyers<em>3 days ago @brightway</em></div></div>
    <div class="tweet"><svg width="10" height="10" viewBox="0 0 10 10" aria-hidden="true"><path d="M1 5l3 3 5-7" stroke="#1ea3cf" stroke-width="1.5" fill="none"/></svg><div>Get a quick quote in minutes with our online form<em>3 days ago @brightway</em></div></div>
    <div class="tweet"><svg width="10" height="10" viewBox="0 0 10 10" aria-hidden="true"><path d="M1 5l3 3 5-7" stroke="#1ea3cf" stroke-width="1.5" fill="none"/></svg><div>Home loan tips for first buyers this spring season<em>2 days ago @brightway</em></div></div>
  </div>
  <div class="abs loc">
    <h4>Location</h4>
    <div>Level 4, 18 Quayside Lane<br>Sydney, NSW 2000</div>
    <div>Call us: <b>1300 482 190</b></div>
    <div>Email: <b>info@brightwaycredit.com.au</b></div>
    <h4 style="margin-top:12px">Stay Connected</h4>
    <div class="social" aria-label="Social links"><span></span><span></span><span></span><span></span></div>
  </div>
</footer>

<div class="abs bottombar">Copyright 2017 Brightway Credit. All Rights Reserved.</div>

</body>
</html>
```